Box packaging design for Bivvo Cheese Knives Set

We would like a box design that is elegant and sophisticated. A box that would be great for gift giving. We are open to your creative ideas. Simple yet chic.

We also want a diagram of the 6 knives on the inside of the top of the lid to show what each knife is used for...you can see an example of it at the below link. We do not want to copy them...this is only for reference.

We will have text on the bottom of the box and "Made in China" somewhere on the box along with the UPC code. The 6 piece knife set is just like the Torvel set in the below link.

https://www.shopvarnel.example/TORVEL-Premium-6-Piece-Cheese-Knife/item/K73QP2XW8R/ref=sr_1_5?s=home-garden&ie=UTF8&qid=1402637719&sr=1-5&keywords=cheese+knives

Bivvo, the name of our company means, "celebrate life."
Our company is all about the Home.
We specialize in very upscale, high-end products for dining, entertaining and cooking.

Attached is the logo that will go on the top of the box. (RGB bivvo.eps)
WE WILL NOT BE USING THE TEXT - (Tools for Discerning Hosts) ONLY the Word Bivvo and the Z.

Attached is a picture of the set of cheese knives that will be going into
the box you will be designing. (Pic of cheese knives.jpg)

Also, attached is a product that we will be selling along with the cheese
knives which will be a second box to design to go along with the first one.
(Cheese marker 5 piece set).

The cheese knife insert card will also need to be designed to go inside the
box. (Cheese knife insert card.png)

On the back of the box we will provide you with a UPC code and where the
UPC code is...please type Made in China as show in the attachment. (UPS
code with Made in China)

Also, on the back of the box ..please add the attached text.

Good luck and best wishes!

1. The Bivvo logo goes on the top of the box.
2. On the inside top of the box we want a diagram of the cheese knives similar to the below link but we can't copy it...if you also look at the card insert attached in the original project instructions you can see the diagram there.

Inside the top of the box will show each knife and what each knife does, for example. Do a silhouette of the knives and under each one will have text with what they are used for.... such as: Hard - Soft - Spread - Serving Fork - etc.

https://lnkpoint.example/images/7Tq4Rm

3. Bottom of box is the same as top size...see attached template for cheese knives box template.... Some text will be on the bottom which i will upload shortly and a UPC code in lower right hand corner with Made in China on it...see attached UPC code for reference.

I attached the cheese marker box template and the insert card template.

Let me know if you have any other questions....and best wishes...Marla

Target Market(s)

Our target audience are people who love to cook, entertain and celebrate life, high-end consumer catering to the luxury market.

Industry/Entity Type

Cooking

Colors
9bcb3b
abd036

Requirements
Must have
• simple yet sophisticated and chic
Nice to have
• We are open to your ideas ...
Should not have
• You can see the attached templates....PLEASE NOTE....the cheese marker template is NOT our design on it...they only sent this over to use the actual template.

```html
<!DOCTYPE html>
<html lang="en">
<head>
<meta charset="utf-8">
<title>Bivvo Cheese Knives Set – Lid Top</title>
<link rel="stylesheet" href="https://fonts.googleapis.com/css2?family=Montserrat:wght@500;700&display=swap">
<style>
  :root {
    --backdrop: #aab4b4;
    --backdrop-light: #d6dcdc;
    --lid-black: #141515;
    --panel-black: #090a0a;
    --band-black: #060707;
    --mint: #66f7d0;
    --white: #ffffff;
  }
  * { margin: 0; padding: 0; box-sizing: border-box; }
  html, body {
    width: 1200px;
    height: 926px;
    overflow: hidden;
  }
  body {
    background: radial-gradient(ellipse at 40% 20%, var(--backdrop-light), var(--backdrop) 70%);
    font-family: "Montserrat", sans-serif;
    position: relative;
  }
  .lid-top {
    position: absolute;
    left: 120px;
    top: 143px;
    width: 960px;
    height: 640px;
    background: var(--lid-black);
    box-shadow: 0 14px 40px rgba(0, 0, 0, 0.25);
  }
  .brand-panel {
    position: absolute;
    left: 350px;
    top: 0;
    width: 260px;
    height: 430px;
    background: var(--panel-black);
    display: flex;
    flex-direction: column;
    align-items: center;
    justify-content: center;
    gap: 34px;
    padding-top: 70px;
  }
  .brand-mark {
    width: 88px;
    height: 88px;
    background: var(--mint);
  }
  .brand-name {
    color: var(--mint);
    font-weight: 500;
    font-size: 44px;
    letter-spacing: 0.4em;
    margin-right: -0.4em;
  }
  .product-band {
    position: absolute;
    left: 470px;
    top: 500px;
    width: 320px;
    height: 64px;
    background: var(--band-black);
    display: flex;
    align-items: center;
    justify-content: center;
  }
  .product-title {
    color: var(--white);
    font-weight: 700;
    font-size: 13px;
    letter-spacing: 0.03em;
    white-space: nowrap;
  }
</style>
</head>
<body>
  <main class="lid-top">
    <section class="brand-panel">
      <div class="brand-mark" aria-hidden="true"></div>
      <div class="brand-name">BIVVO</div>
    </section>
    <section class="product-band">
      <p class="product-title">PREMIUM 6-PIECES CHEESE KNIVES SET</p>
    </section>
  </main>
</body>
</html>
```